Business card design for online Mandarin Learning School

We need a business card design for our online language learning school called "Maple Bridge Online for Mandarin Learning". Our existing website is https://www.maplebridgeonline.com
We have our logo already. We would like to see our business card design that can make our online teaching services to be innovative, young, energetic and fun to learn. Prefer to have a certain level of color matching with our website. Apart from "Maple Bridge Online", need to specifically state "for Mandarin Learning" as well on the business card.

```html
<!DOCTYPE html>
<html lang="en">
<head>
<meta charset="utf-8">
<title>Maple Bridge Online – Business Card</title>
<link rel="stylesheet" href="https://fonts.googleapis.com/css2?family=Cinzel:wght@400&family=Montserrat:wght@400;500&family=Lato:wght@400&display=swap">
<style>
  :root {
    --teal: #0aa9b7;
    --teal-text: #1aa3b0;
    --coral: #e4605f;
    --paper: #ededef;
    --ink-grey: #6f6f72;
    --rule: #b9b9bc;
    --stage: #2b2b2d;
    --white: #ffffff;
  }
  * { box-sizing: border-box; margin: 0; padding: 0; }
  html, body {
    width: 1200px; height: 1200px; overflow: hidden;
    background: var(--stage);
  }
  .canvas { position: relative; width: 1200px; height: 1200px; }

  .card { position: absolute; box-shadow: 0 10px 24px rgba(0,0,0,.45); }

  /* Front */
  .card-front {
    left: 187px; top: 86px; width: 823px; height: 475px;
    background: var(--teal); color: var(--white); text-align: center;
  }
  .card-front .mark-dot {
    position: absolute; left: 50%; top: 238px;
    width: 16px; height: 16px; margin-left: -8px;
    border-radius: 50%; background: var(--white);
  }
  .card-front .wordmark {
    position: absolute; left: 0; right: 0; top: 268px;
    font-family: "Cinzel", serif; font-size: 50px; letter-spacing: 1px;
  }
  .card-front .tagline {
    position: absolute; left: 0; right: 0; top: 404px;
    font-family: "Montserrat", sans-serif; font-weight: 500; font-size: 25px; letter-spacing: .5px;
  }

  /* Back */
  .card-back {
    left: 186px; top: 640px; width: 839px; height: 468px;
    background: var(--paper);
  }
  .card-back .mark-dot {
    position: absolute; right: 147px; top: 88px;
    width: 16px; height: 16px; border-radius: 50%; background: var(--coral);
  }
  .card-back .wordmark {
    position: absolute; right: 48px; top: 160px;
    font-family: "Cinzel", serif; font-size: 38px; color: var(--teal-text);
    letter-spacing: .5px;
  }
  .holder { position: absolute; left: 46px; top: 248px; }
  .holder .name {
    font-family: "Montserrat", sans-serif; font-weight: 400; font-size: 34px;
    color: var(--teal-text); line-height: 1;
  }
  .holder .role {
    margin-top: 8px; font-family: "Lato", sans-serif; font-size: 19px; color: var(--ink-grey);
  }
  .divider {
    position: absolute; left: 46px; right: 48px; top: 330px;
    border-top: 1.5px solid var(--rule);
  }
  .contacts {
    position: absolute; left: 46px; top: 346px; list-style: none;
    font-family: "Lato", sans-serif; font-size: 19.5px; color: var(--ink-grey);
  }
  .contacts li { display: flex; align-items: center; height: 28.5px; }
  .contacts svg { width: 14px; height: 14px; margin-right: 4px; flex: none; }
  .address {
    position: absolute; right: 48px; top: 374px; text-align: right;
    font-family: "Lato", sans-serif; font-size: 19.5px; color: var(--ink-grey); line-height: 26.5px;
  }
</style>
</head>
<body>
<main class="canvas">

  <section class="card card-front" aria-label="Business card front">
    <span class="mark-dot"></span>
    <h1 class="wordmark">MAPLE BRIDGE</h1>
    <p class="tagline">For Mandarin Learning</p>
  </section>

  <section class="card card-back" aria-label="Business card back">
    <span class="mark-dot"></span>
    <p class="wordmark">MAPLE BRIDGE</p>

    <div class="holder">
      <p class="name">Daniel Reyes</p>
      <p class="role">Co-Founder | Partner</p>
    </div>

    <div class="divider"></div>

    <ul class="contacts">
      <li>
        <svg viewBox="0 0 16 16" aria-hidden="true"><path fill="#1aa3b0" d="M3.6 1.5l2.3 2.6-1.3 1.7c.9 2 2.4 3.5 4.4 4.5l1.7-1.3 2.6 2.3-1.2 2.4C7.4 13.5 2.6 8.7 1.3 3z"/></svg>
        +65 555-0142
      </li>
      <li>
        <svg viewBox="0 0 16 16" aria-hidden="true"><rect x="1" y="3.5" width="14" height="9" fill="#e4605f"/><path d="M1 3.5l7 5.5 7-5.5" fill="none" stroke="#fff" stroke-width="1.2"/></svg>
        support@MapleBridgeOnline.com
      </li>
      <li>
        <svg viewBox="0 0 16 16" aria-hidden="true"><g fill="none" stroke="#1aa3b0" stroke-width="1.2"><circle cx="8" cy="8" r="6.5"/><ellipse cx="8" cy="8" rx="3" ry="6.5"/><path d="M1.5 8h13M2.5 5h11M2.5 11h11"/></g></svg>
        www.maplebridgeonline.com
      </li>
    </ul>

    <address class="address" style="font-style:normal">
      your street / Road, Suite 200<br>
      your country name
    </address>
  </section>

</main>
</body>
</html>
```